Front cover for Bathroom Catalogue

We want to see some concepts for a new front cover of our next catalogue. Attached is the existing.

The following must be included on the cover:
1. "Corlen Vaska" logo
2. x9 product category Icons (can display just 9 or turn into a pattern like exisiting)
3. Ideally we include the Water Splash Pattern in some capacity, also attached (Feel free to add colour to the splash/edit or incorporate the splash into something else).

We also wish to add some colour/colours to make it stand out from the previous cover too.

Target Market(s)

Home owners, renovators, designers, architects

Industry/Entity Type

Bathroom

Font styles to use
Sans Serif

Colors
0054AA
0677BA
7BADD7
CADEEF
E8F1F8
0094D4
00A9DD
6FCCEA
C7EBF8
E9F6FB

Requirements
Must have
• Colour, "Corlen Vaska" logo, x9 product category icons.
Nice to have
• Possibly some colour to make it stand out.

```html
<!DOCTYPE html>
<html lang="en">
<head>
<meta charset="utf-8">
<title>Corlen Vaska – Catalogue Cover</title>
<link href="https://fonts.googleapis.com/css2?family=Outfit:wght@300;400;600&display=swap" rel="stylesheet">
<style>
  :root {
    --stage: #dcdcdc;
    --navy: #0054AA;
    --ocean: #0677BA;
    --sky: #7BADD7;
    --mist: #CADEEF;
    --foam: #E8F1F8;
    --aqua: #00A9DD;
    --aqua-soft: #6FCCEA;
    --white: #ffffff;
    --ink: #2a2a2a;
  }
  * { margin: 0; padding: 0; box-sizing: border-box; }
  html, body { width: 1040px; height: 1200px; overflow: hidden; }
  body { background: var(--stage); font-family: "Outfit", sans-serif; position: relative; }

  .cover {
    position: absolute; left: 131px; top: 50px;
    width: 778px; height: 1100px; overflow: hidden;
    background: var(--mist);
  }
  .cover__splash {
    position: absolute; inset: 0;
    background:
      radial-gradient(ellipse 420px 460px at 332px 399px, var(--ocean) 0%, var(--sky) 30%, var(--mist) 75%, rgba(202,222,239,0) 100%),
      linear-gradient(160deg, var(--mist) 0%, #bcd6ee 55%, var(--mist) 100%);
  }
  .cover__column {
    position: absolute; left: 354px; top: 0; width: 345px; height: 100%;
    background: rgba(255,255,255,0.55);
  }
  .cover__lower-band {
    position: absolute; left: 0; top: 674px; width: 100%; height: 345px;
    background: rgba(255,255,255,0.55);
  }
  .cover__footer-band {
    position: absolute; left: 0; top: 1019px; width: 100%; height: 81px;
    background: var(--mist);
  }
  .cover__footer-band::after {
    content: ""; position: absolute; left: 354px; top: 0; width: 345px; height: 100%;
    background: var(--foam);
  }

  .brand {
    position: absolute; left: 510px; top: 333px;
    transform: translate(-50%, -50%) rotate(-90deg);
    white-space: nowrap;
    font-weight: 300; font-size: 84px; letter-spacing: 1px;
    color: var(--ink);
  }

  .categories {
    position: absolute; left: 354px; top: 674px; width: 345px; height: 345px;
    background: var(--white);
  }
  .categories__icon {
    position: absolute; width: 48px; height: 48px;
    transform: translate(-50%, -50%);
    fill: var(--ink);
  }

  .issue {
    position: absolute; right: 108px; top: 1026px;
    display: flex; align-items: baseline; gap: 12px;
    color: var(--ink);
  }
  .issue__number { font-size: 18px; font-weight: 400; }
  .issue__year { font-size: 27px; font-weight: 300; color: var(--ocean); }
  .website {
    position: absolute; right: 108px; top: 1063px;
    font-size: 23px; font-weight: 600; color: var(--navy); letter-spacing: 0.3px;
  }
</style>
</head>
<body>
  <main class="cover">
    <div class="cover__splash" role="img" aria-label="Blue water splash pattern swirling around a drain"></div>
    <div class="cover__column"></div>
    <div class="cover__lower-band"></div>
    <div class="cover__footer-band"></div>

    <h1 class="brand">Corlen Vaska</h1>

    <section class="categories" aria-label="Product categories">
      <svg class="categories__icon" style="left:64px;top:69px" viewBox="0 0 48 48" aria-label="Basins"><path d="M2 20h44c0 8-6 13-12 14v12H22v-9C12 36 3 30 2 20z"/><rect x="30" y="8" width="4" height="12"/><path d="M28 6h9v3h-9z"/></svg>
      <svg class="categories__icon" style="left:169px;top:69px" viewBox="0 0 48 48" aria-label="Vanities"><rect x="4" y="4" width="40" height="3"/><path d="M6 10h36v30H6z M12 17h24v3H12z M12 29h24v3H12z" fill-rule="evenodd"/><rect x="6" y="40" width="3" height="5"/><rect x="39" y="40" width="3" height="5"/></svg>
      <svg class="categories__icon" style="left:266px;top:69px" viewBox="0 0 48 48" aria-label="Baths"><rect x="1" y="16" width="46" height="4" rx="1"/><path d="M3 22h42l-3 12H6z"/><rect x="10" y="33" width="4" height="5" rx="2"/><rect x="34" y="33" width="4" height="5" rx="2"/></svg>
      <svg class="categories__icon" style="left:64px;top:165px" viewBox="0 0 48 48" aria-label="Tapware"><path d="M18 8l20 4v6H18z"/><rect x="22" y="18" width="14" height="28"/><path d="M6 24h18v6H6z"/></svg>
      <svg class="categories__icon" style="left:169px;top:165px" viewBox="0 0 48 48" aria-label="Toilets"><rect x="32" y="2" width="10" height="24" rx="2"/><path d="M4 26h38v10c0 6-4 10-10 10H14v-8C8 37 4 32 4 26z"/></svg>
      <svg class="categories__icon" style="left:266px;top:165px" viewBox="0 0 48 48" aria-label="Showers"><path d="M24 2a13 13 0 1 1 0 26 13 13 0 0 1 0-26z M19 9a2 2 0 1 0 0.01 0z M24 8a2 2 0 1 0 .01 0z M29 9a2 2 0 1 0 .01 0z M18 15a2 2 0 1 0 .01 0z M24 14a2 2 0 1 0 .01 0z M30 15a2 2 0 1 0 .01 0z M20 20a2 2 0 1 0 .01 0z M28 20a2 2 0 1 0 .01 0z" fill-rule="evenodd"/><rect x="22" y="28" width="4" height="19" rx="2"/></svg>
      <svg class="categories__icon" style="left:64px;top:263px" viewBox="0 0 48 48" aria-label="Shower enclosures"><path d="M24 2l18 8v28L24 46 6 38V10z" fill="none" stroke="var(--ink)" stroke-width="2.5" stroke-linejoin="round"/><path d="M6 10l18 8 18-8M24 18v28" fill="none" stroke="var(--ink)" stroke-width="2"/><rect x="33" y="22" width="2.5" height="10"/></svg>
      <svg class="categories__icon" style="left:169px;top:263px" viewBox="0 0 48 48" aria-label="Accessories"><rect x="17" y="2" width="12" height="5" rx="1"/><path d="M29 4h6c3 0 5 1 6 3l-2 1c-1-1-2-1-4-1h-6z"/><rect x="20" y="7" width="6" height="7"/><rect x="12" y="14" width="22" height="32" rx="3"/></svg>
      <svg class="categories__icon" style="left:266px;top:263px" viewBox="0 0 48 48" aria-label="Sink mixers"><path d="M20 30V16a12 12 0 0 1 24 0v4h-5v-4a7 7 0 0 0-14 0v14z"/><circle cx="20" cy="34" r="5" fill="none" stroke="var(--ink)" stroke-width="3"/><path d="M10 22l7 8-2 2-7-8z"/><rect x="16" y="38" width="8" height="8"/></svg>
    </section>

    <div class="issue"><span class="issue__number">ISSUE 26</span><span class="issue__year">2024/25</span></div>
    <p class="website">VASKABATH.CO.NZ</p>
  </main>
</body>
</html>
```